Mardi Gras 2013 Design Project

We have a design with elements that we want to retain. However, we need to take what we have and give it a creative BOOST!

Requirements
Must have
• Colors must stay, "KT" logo must stay,
Copy must remain (except - "Requests Your Presence" and small copy in bottom right corner);
Seal must remain, "9th Annual Velvet Lantern Gala" frame text can be modified but should resemble;
Gotham font to remain
Nice to have
• Any new Mardi Gras element - like a mask or beads - but can not over shadow copy

```html
<!DOCTYPE html>
<html lang="en">
<head>
<meta charset="utf-8">
<title>9th Annual Velvet Lantern Gala – Invitation</title>
<link rel="stylesheet" href="https://fonts.googleapis.com/css2?family=Cinzel:wght@400;700&display=swap">
<style>
  :root {
    --page: #ffffff;
    --violet-deep: #2a1670;
    --violet: #4b2fb0;
    --violet-light: #7a5be0;
    --gold: #f2b21c;
    --orange: #ff8a10;
    --green: #39b54a;
    --seal-gold: #f3d94c;
    --line-green: #7fc35a;
  }
  * { margin: 0; padding: 0; box-sizing: border-box; }
  html, body {
    width: 1200px; height: 900px; overflow: hidden;
    background: var(--page);
    font-family: "Cinzel", "Times New Roman", serif;
  }
  .canvas {
    position: relative; width: 1200px; height: 900px;
    display: flex; align-items: center; justify-content: center; gap: 60px;
  }
  .card {
    position: relative; width: 520px; height: 320px;
    background: linear-gradient(135deg, var(--violet-light) 0%, var(--violet) 45%, var(--violet-deep) 100%);
    overflow: hidden;
  }
  /* front */
  .card-front__header {
    position: absolute; left: 22px; top: 18px; width: 476px; height: 118px;
    display: flex; gap: 16px;
  }
  .brand {
    width: 170px; height: 118px;
    background: rgba(255,255,255,0.08);
    padding: 10px 12px;
    display: flex; flex-direction: column; align-items: flex-start; gap: 6px;
  }
  .brand__row { display: flex; align-items: center; gap: 8px; }
  .brand__name { color: var(--gold); font-size: 26px; font-weight: 700; line-height: 1; }
  .brand__org { color: var(--gold); font-size: 8px; line-height: 1.25; width: 90px; }
  .seal-badge { width: 48px; height: 48px; border-radius: 50%; background: var(--seal-gold); margin-left: 50px; }
  .title-frame {
    flex: 1; height: 118px;
    background: linear-gradient(160deg, rgba(170,140,240,0.55), rgba(90,60,190,0.35));
    padding: 12px 18px;
    display: flex; flex-direction: column; justify-content: center;
  }
  .title-frame__kicker { color: var(--gold); font-size: 16px; font-weight: 700; letter-spacing: 1px; }
  .title-frame__name { color: var(--green); font-size: 26px; font-weight: 700; line-height: 1.05; }
  .divider {
    position: absolute; left: 22px; top: 150px; width: 476px; height: 1px;
    background: var(--line-green);
  }
  .details {
    position: absolute; left: 30px; top: 160px;
    color: var(--gold); line-height: 1.15;
  }
  .details__day { font-size: 22px; font-weight: 700; }
  .details__date { font-size: 14px; }
  .details__at { font-size: 11px; }
  .details__venue { font-size: 17px; color: var(--gold); }
  .details__venue--big { font-size: 22px; }
  .details__street { font-size: 10px; }
  .details__city { font-size: 26px; color: var(--orange); margin-top: 2px; }
  /* back */
  .card-back__band {
    position: absolute; left: 0; top: 95px; width: 100%; height: 130px;
    border-top: 1px solid rgba(255,255,255,0.15);
    border-bottom: 1px solid rgba(255,255,255,0.15);
    display: flex; align-items: center; justify-content: center; gap: 14px;
  }
  .card-back__mark { color: var(--gold); font-size: 84px; font-weight: 700; line-height: 1; }
  .card-back__square { width: 18px; height: 18px; background: var(--gold); }
</style>
</head>
<body>
<main class="canvas">
  <section class="card card-front" aria-label="Invitation front">
    <div class="card-front__header">
      <div class="brand">
        <div class="brand__row">
          <span class="brand__name">KT</span>
          <span class="brand__org">The Society of Kestrel Tower Alumni</span>
        </div>
        <div class="seal-badge" role="img" aria-label="Society seal"></div>
      </div>
      <div class="title-frame">
        <span class="title-frame__kicker">9th Annual</span>
        <span class="title-frame__name">Velvet Lantern Gala</span>
      </div>
    </div>
    <div class="divider"></div>
    <div class="details">
      <div class="details__day">Saturday</div>
      <div class="details__date">January 26, 2013</div>
      <div class="details__date">7PM – 12AM</div>
      <div class="details__at">at the</div>
      <div class="details__venue">Harbor Crest</div>
      <div class="details__venue details__venue--big">Convention Center</div>
      <div class="details__street">1800 Lantern Way Concourse</div>
      <div class="details__city">Maple Falls, Georgia</div>
    </div>
  </section>

  <section class="card card-back" aria-label="Invitation back">
    <div class="card-back__band">
      <span class="card-back__mark">KT</span>
      <span class="card-back__square"></span>
    </div>
  </section>
</main>
</body>
</html>
```